Harbinger Slabworks, Inc. Business Card

Create a business card that is eye catching and based around concrete sawcutting. I've attached our current business card and logo for reference. We like aspects of the current business card, but it is starting to feel very loud and lost. We would like something that is still fun but is more modern and streamlined.

```html
<!DOCTYPE html>
<html lang="en">
<head>
<meta charset="utf-8">
<title>Harbinger Slabworks, Inc. Business Card</title>
<link rel="stylesheet" href="https://fonts.googleapis.com/css2?family=Montserrat:wght@400;500;700&display=swap">
<style>
  :root {
    --stage: #2a2a2c;
    --navy: #1f2a56;
    --red: #c8171b;
    --gold: #f7c31a;
    --white: #ffffff;
  }
  * { box-sizing: border-box; margin: 0; padding: 0; }
  html, body { width: 1200px; height: 1200px; overflow: hidden; }
  body {
    background: var(--stage);
    font-family: "Montserrat", Arial, sans-serif;
    color: var(--white);
    position: relative;
  }
  .card {
    position: absolute;
    top: 232px;
    width: 420px;
    height: 735px;
    background: var(--navy);
    border-radius: 26px;
    overflow: hidden;
  }
  .card--front { left: 150px; }
  .card--back { left: 630px; }

  .brand {
    display: flex;
    flex-direction: column;
    align-items: center;
    gap: 16px;
  }
  .brand__dot {
    width: 84px; height: 84px;
    border-radius: 50%;
    background: var(--red);
  }
  .brand__name {
    font-weight: 700;
    font-size: 24px;
    letter-spacing: 2px;
    text-align: center;
    line-height: 1.25;
    color: var(--white);
  }
  .card--front .brand {
    position: absolute;
    top: 78px; left: 0; right: 0;
  }

  .name-band {
    position: absolute;
    top: 320px; left: 0; right: 0;
    height: 104px;
    background: var(--red);
    display: flex;
    flex-direction: column;
    align-items: center;
    justify-content: center;
    gap: 4px;
  }
  .name-band__name {
    color: var(--gold);
    font-weight: 700;
    font-size: 30px;
    letter-spacing: 1.5px;
  }
  .name-band__title {
    font-size: 18px;
    font-weight: 400;
  }

  .contact {
    position: absolute;
    top: 452px; left: 0; right: 0;
    display: flex;
    flex-direction: column;
    align-items: center;
  }
  .contact__rule-row {
    display: flex;
    align-items: center;
    gap: 14px;
    margin-bottom: 14px;
  }
  .rule { height: 1px; background: var(--gold); }
  .contact__rule-row .rule { width: 92px; }
  .icons { display: flex; gap: 8px; }
  .icon {
    width: 22px; height: 22px;
    border-radius: 4px;
    background: var(--red);
    display: flex; align-items: center; justify-content: center;
  }
  .icon svg { width: 13px; height: 13px; }
  .contact__lines {
    list-style: none;
    text-align: center;
    font-size: 16.5px;
    line-height: 1.62;
    letter-spacing: 0.4px;
  }
  .contact__divider { width: 300px; margin: 14px 0 12px; }
  .address {
    font-style: normal;
    text-align: center;
    font-size: 17px;
    line-height: 1.55;
    letter-spacing: 0.5px;
  }

  .card--back .brand {
    position: absolute;
    top: 270px; left: 40px; width: 260px;
  }
  .services {
    position: absolute;
    right: 40px; top: 60px; bottom: 60px;
    writing-mode: vertical-rl;
    transform: rotate(180deg);
    display: flex;
    flex-direction: column;
    justify-content: center;
    align-items: center;
    gap: 10px;
  }
  .services__list {
    font-size: 17px;
    letter-spacing: 0.4px;
    white-space: nowrap;
  }
  .services__phone {
    color: var(--gold);
    font-weight: 500;
    font-size: 20px;
    letter-spacing: 0.5px;
    white-space: nowrap;
  }
</style>
</head>
<body>

<section class="card card--front" aria-label="Business card front">
  <div class="brand">
    <span class="brand__dot"></span>
    <span class="brand__name">HARBINGER<br>SLABWORKS</span>
  </div>

  <div class="name-band">
    <span class="name-band__name">MARLOWE KESTREL</span>
    <span class="name-band__title">Owner/CEO</span>
  </div>

  <div class="contact">
    <div class="contact__rule-row">
      <span class="rule"></span>
      <div class="icons">
        <span class="icon"><svg viewBox="0 0 16 16"><path fill="#fff" d="M3.5 1.5l2.5 2.8-1.4 1.6c.9 2 2.4 3.5 4.4 4.4l1.6-1.4 2.8 2.5-1.5 2.2C6.6 13.4 2.6 9.4 1.4 3z"/></svg></span>
        <span class="icon"><svg viewBox="0 0 16 16"><rect x="4" y="1" width="8" height="14" rx="1.5" fill="none" stroke="#fff" stroke-width="1.6"/><circle cx="8" cy="12.5" r="1" fill="#fff"/></svg></span>
        <span class="icon"><svg viewBox="0 0 16 16"><rect x="1.5" y="3.5" width="13" height="9" fill="none" stroke="#fff" stroke-width="1.5"/><path d="M1.5 3.5L8 9l6.5-5.5" fill="none" stroke="#fff" stroke-width="1.5"/></svg></span>
        <span class="icon"><svg viewBox="0 0 16 16"><circle cx="8" cy="8" r="6.3" fill="none" stroke="#fff" stroke-width="1.5"/><path d="M1.7 8h12.6M8 1.7c-3 3.5-3 9.1 0 12.6M8 1.7c3 3.5 3 9.1 0 12.6" fill="none" stroke="#fff" stroke-width="1.2"/></svg></span>
      </div>
      <span class="rule"></span>
    </div>
    <ul class="contact__lines">
      <li>855.555.0142</li>
      <li>973.555.0187</li>
      <li>marlowe@harbingerslabworks.com</li>
      <li>www.harbingerslabworks.com</li>
    </ul>
    <span class="rule contact__divider"></span>
    <address class="address">48 N. Alder Row<br>Fairhaven, NJ 07999</address>
  </div>
</section>

<section class="card card--back" aria-label="Business card back">
  <div class="brand">
    <span class="brand__dot"></span>
    <span class="brand__name">HARBINGER<br>SLABWORKS</span>
  </div>
  <div class="services">
    <span class="services__phone">855-SLABCUT</span>
    <span class="services__list">Wall Sawing • Core Drilling • Slab Sawing • Breaking &amp; Removal</span>
  </div>
</section>

</body>
</html>
```